PeachLoft: Smart Quotes for Wine Lovers

Hello. I am completing book of quotes for wine lovers. Need the text formatted so that it is easy to read and aesthetically pleasing...modern, clean, smart. Number the pages. The cover is complete. Book is small square. 7.5 by 7.5 inches. If you want to show me first few pages that would be awesome. Thank you!
Updates

I edited the quotes so if you downloaded first ones, please grab these ones instead, thank you! 

Target Market(s)

wine lovers. Urban. Modern.

Industry/Entity Type

Quotes

Requirements
Should not have
• No color. black and white only.

```html
<!DOCTYPE html>
<html lang="en">
<head>
<meta charset="utf-8">
<title>PeachLoft – Smart Quotes for Wine Lovers, pages 3–4</title>
<link rel="stylesheet" href="https://fonts.googleapis.com/css2?family=Poppins:ital,wght@0,400;0,600;1,600&display=swap">
<style>
  :root {
    --backdrop: #4d4d4d;
    --paper: #ffffff;
    --ink: #1a1a1a;
    --ink-soft: #3a3a3a;
    --ghost: #f1f1f1;
    --signature-tone: #d9d9d9;
    --gutter-line: #bdbdbd;
  }
  * { box-sizing: border-box; margin: 0; padding: 0; }
  html, body {
    width: 1200px; height: 800px; overflow: hidden;
    background: var(--backdrop);
    font-family: "Poppins", sans-serif;
    color: var(--ink);
  }
  .spread {
    position: absolute; left: 60px; top: 30px;
    width: 1080px; height: 740px;
    display: flex;
    box-shadow: 0 6px 24px rgba(0,0,0,.35);
  }
  .page {
    position: relative;
    width: 540px; height: 740px;
    background: var(--paper);
    padding: 58px 48px 0 62px;
    overflow: hidden;
  }
  .page--left { border-right: 1px solid var(--gutter-line); }
  .page-ghost {
    position: absolute; left: 90px; top: 110px;
    width: 360px; height: 520px;
    border-radius: 48% 48% 40% 40%;
    background: radial-gradient(ellipse at 50% 40%, var(--ghost), rgba(241,241,241,0) 72%);
  }
  .quote {
    position: relative;
    margin-bottom: 64px;
    padding-left: 34px;
  }
  .quote__mark {
    position: absolute; left: 0; top: -10px;
    font-weight: 600; font-size: 44px; line-height: 1;
  }
  .quote__text {
    font-style: italic; font-weight: 600;
    font-size: 18.5px; line-height: 1.25;
    letter-spacing: -0.2px;
  }
  .attribution {
    display: flex; align-items: flex-start;
    margin-top: 8px;
  }
  .attribution__author {
    display: flex; align-items: center;
    width: 150px; flex-shrink: 0;
    font-size: 15px;
  }
  .signature {
    display: inline-block;
    width: 110px; height: 26px; margin-left: 6px;
    border-radius: 3px;
    background: var(--signature-tone);
  }
  .attribution__bio {
    font-size: 9.5px; line-height: 1.35;
    color: var(--ink-soft);
    max-width: 190px;
  }
  .page-number {
    position: absolute; right: 40px; bottom: 28px;
    font-weight: 600; font-size: 15px;
  }
</style>
</head>
<body>
<main class="spread">

  <section class="page page--left">
    <div class="page-ghost" role="img" aria-label="Faint wine glass decoration"></div>

    <article class="quote">
      <span class="quote__mark">“</span>
      <p class="quote__text">The connoisseur does not drink<br>wine but tastes its secrets.</p>
      <div class="attribution">
        <div class="attribution__author">–<span class="signature" role="img" aria-label="Handwritten signature of Silvano Ferran"></span></div>
        <p class="attribution__bio">Silvano Ferran Montsenet, known to friends as the Cellar Poet (1911 – 1976) Catalan Vintner and Diarist.</p>
      </div>
    </article>

    <article class="quote">
      <span class="quote__mark">“</span>
      <p class="quote__text">Wine is the divine juice of September.</p>
      <div class="attribution">
        <div class="attribution__author">–<span class="signature" role="img" aria-label="Handwritten signature of Valcourt"></span></div>
        <p class="attribution__bio">Lucien-Marie Arnaud known by his “nom de plume” Valcourt. (1842 – 1907) Burgundy Wine Merchant, Essayist and Traveller.</p>
      </div>
    </article>

    <article class="quote">
      <span class="quote__mark">“</span>
      <p class="quote__text">The discovery of a good wine is<br>increasingly better for mankind<br>than the discovery of a new star.</p>
      <div class="attribution">
        <div class="attribution__author">–<span class="signature" role="img" aria-label="Handwritten signature of Lorenzo Carrara"></span></div>
        <p class="attribution__bio">Lorenzo Carrara (1868 – 1931) Piedmontese Vine Grower, Cooper, Botanist, Amateur Astronomer, Mapmaker and Author of Cellar Notebooks.</p>
      </div>
    </article>

    <article class="quote">
      <span class="quote__mark">“</span>
      <p class="quote__text">Be careful to trust a person who<br>does not like wine.</p>
      <div class="attribution">
        <div class="attribution__author">–<span class="signature" role="img" aria-label="Handwritten signature of Konrad Maier"></span></div>
        <p class="attribution__bio">Konrad Heinrich Maier (1880 – 1952) Rhine Valley Innkeeper, Sommelier, Local Historian and Newspaper Columnist.</p>
      </div>
    </article>

    <span class="page-number">3</span>
  </section>

  <section class="page page--right">
    <div class="page-ghost" role="img" aria-label="Faint wine glass decoration"></div>

    <article class="quote">
      <span class="quote__mark">“</span>
      <p class="quote__text">The connoisseur does not drink<br>wine but tastes its secrets.</p>
      <div class="attribution">
        <div class="attribution__author">–<span class="signature" role="img" aria-label="Handwritten signature of Silvano Ferran"></span></div>
        <p class="attribution__bio">Silvano Ferran Montsenet, known to friends as the Cellar Poet (1911 – 1976) Catalan Vintner and Diarist.</p>
      </div>
    </article>

    <article class="quote">
      <span class="quote__mark">“</span>
      <p class="quote__text">Wine is the divine juice of September.</p>
      <div class="attribution">
        <div class="attribution__author">–<span class="signature" role="img" aria-label="Handwritten signature of Valcourt"></span></div>
        <p class="attribution__bio">Lucien-Marie Arnaud known by his “nom de plume” Valcourt. (1842 – 1907) Burgundy Wine Merchant, Essayist and Traveller.</p>
      </div>
    </article>

    <article class="quote">
      <span class="quote__mark">“</span>
      <p class="quote__text">The discovery of a good wine is<br>increasingly better for mankind<br>than the discovery of a new star.</p>
      <div class="attribution">
        <div class="attribution__author">–<span class="signature" role="img" aria-label="Handwritten signature of Lorenzo Carrara"></span></div>
        <p class="attribution__bio">Lorenzo Carrara (1868 – 1931) Piedmontese Vine Grower, Cooper, Botanist, Amateur Astronomer, Mapmaker and Author of Cellar Notebooks.</p>
      </div>
    </article>

    <article class="quote">
      <span class="quote__mark">“</span>
      <p class="quote__text">Be careful to trust a person who<br>does not like wine.</p>
      <div class="attribution">
        <div class="attribution__author">–<span class="signature" role="img" aria-label="Handwritten signature of Konrad Maier"></span></div>
        <p class="attribution__bio">Konrad Heinrich Maier (1880 – 1952) Rhine Valley Innkeeper, Sommelier, Local Historian and Newspaper Columnist.</p>
      </div>
    </article>

    <span class="page-number">4</span>
  </section>

</main>
</body>
</html>
```